NEW YORK Plumbing/utility company 10 year anniversary business card

Looking For simple back and front business card would like to include a few things in description
We offer 24/7 emergency service
residential
commercial
industrial
municipal
services offered
Plumbing
hydro excavation
hydro jetting
Well pumps
Sewer pumps
water mains
sewer mains

```html
<!DOCTYPE html>
<html lang="en">
<head>
<meta charset="utf-8">
<title>Riverbend Water &amp; Sewer – Business Card</title>
<link href="https://fonts.googleapis.com/css2?family=Archivo+Black&family=Montserrat:wght@400;500;600;700&display=swap" rel="stylesheet">
<style>
  :root {
    --blue: #1d5fa8;
    --blue-dark: #174f8e;
    --red: #e3232c;
    --white: #ffffff;
    --ink: #4a4a4a;
    --page: #eef0f3;
    --wave-a: #fbe3dc;
    --wave-b: #fdf3ef;
  }
  * { box-sizing: border-box; margin: 0; padding: 0; }
  html, body { width: 1200px; height: 873px; overflow: hidden; background: var(--page); }
  body { position: relative; font-family: "Montserrat", sans-serif; }

  .card {
    position: absolute;
    width: 540px; height: 309px;
    top: 282px;
    overflow: hidden;
    border-radius: 4px;
    box-shadow: 0 10px 30px rgba(0,0,0,.15);
  }

  /* ---------- Front: services ---------- */
  .card--front { left: 40px; background: var(--white); }
  .front__tab {
    position: absolute; width: 26px; height: 92px; background: var(--blue);
  }
  .front__tab--left { left: 0; top: 22px; border-radius: 0 14px 14px 0; }
  .front__tab--right { right: 0; bottom: 22px; border-radius: 14px 0 0 14px; }
  .front__wave {
    position: absolute; left: 0; bottom: 0; width: 330px; height: 150px;
    background: radial-gradient(ellipse at 40% 80%, var(--wave-a), var(--wave-b) 55%, transparent 75%);
  }
  .brand {
    position: absolute; font-family: "Montserrat", sans-serif; font-weight: 700;
    color: var(--blue); text-transform: uppercase; letter-spacing: 1px; line-height: 1.15;
    display: flex; align-items: center; gap: 8px;
  }
  .brand__dot { width: 14px; height: 14px; border-radius: 50%; background: var(--red); flex: none; }
  .front__brand { left: 240px; top: 26px; font-size: 17px; }
  .section-title {
    position: absolute; font-family: "Archivo Black", sans-serif; color: var(--blue);
    text-transform: uppercase; letter-spacing: .5px;
  }
  .front__services-title { left: 48px; top: 84px; font-size: 19px; }
  .service-list {
    position: absolute; left: 48px; top: 116px; list-style: none;
    display: grid; grid-template-columns: repeat(3, 140px); row-gap: 7px;
    font-size: 11.5px; color: var(--ink);
  }
  .service-list li { display: flex; align-items: center; gap: 6px; }
  .tick { width: 14px; height: 14px; flex: none; }
  .front__emergency-title { left: 48px; top: 196px; font-size: 19px; }
  .sector-list {
    position: absolute; left: 48px; top: 236px; list-style: none;
    display: flex; gap: 22px; font-size: 12.5px; color: var(--ink);
  }
  .sector-list li { display: flex; align-items: center; gap: 6px; }
  .star { width: 14px; height: 14px; flex: none; }

  /* ---------- Back: contact ---------- */
  .card--back { left: 620px; background: var(--blue); }
  .back__shape { position: absolute; inset: 0; }
  .back__notch {
    position: absolute; left: 0; top: 28px; width: 34px; height: 108px;
    background: var(--white); border-radius: 0 12px 12px 0;
    display: flex; flex-direction: column; align-items: center; justify-content: space-around; padding: 8px 0;
  }
  .contact-icon {
    width: 16px; height: 16px; border-radius: 50%; background: var(--red);
    display: flex; align-items: center; justify-content: center;
  }
  .contact-icon svg { width: 9px; height: 9px; }
  .back__name {
    position: absolute; left: 50px; top: 22px; font-size: 20px; font-weight: 700;
    color: var(--white); text-transform: uppercase; letter-spacing: 1px;
  }
  .back__role { position: absolute; left: 50px; top: 50px; font-size: 12px; color: var(--white); }
  .contact-list {
    position: absolute; left: 50px; top: 82px; list-style: none;
    font-size: 11px; color: #dce7f5; line-height: 1.75; font-weight: 400;
  }
  .back__address {
    position: absolute; left: 50px; top: 176px; font-size: 10.5px; color: var(--white); line-height: 1.7; font-weight: 500;
  }
  .back__brand { right: 26px; top: 200px; font-size: 15px; }
  .social {
    position: absolute; right: 30px; top: 248px; display: flex; gap: 12px;
  }
  .social span { width: 20px; height: 20px; border-radius: 50%; background: #9a9a9a; }
</style>
</head>
<body>

  <!-- Front -->
  <section class="card card--front" aria-label="Front of card: services">
    <div class="front__wave" role="img" aria-label="Soft flowing line pattern in pale peach tones"></div>
    <div class="front__tab front__tab--left"></div>
    <div class="front__tab front__tab--right"></div>

    <div class="brand front__brand"><span class="brand__dot"></span><span>Riverbend<br>Water &amp; Sewer</span></div>

    <h2 class="section-title front__services-title">Services Offered</h2>
    <ul class="service-list">
      <li><svg class="tick" viewBox="0 0 14 14"><rect x="1" y="1" width="12" height="12" fill="none" stroke="#1d5fa8" stroke-width="1.2"/><path d="M3 7l3 3 6-8" fill="none" stroke="#28a8e0" stroke-width="1.8"/></svg>Plumbing</li>
      <li><svg class="tick" viewBox="0 0 14 14"><rect x="1" y="1" width="12" height="12" fill="none" stroke="#1d5fa8" stroke-width="1.2"/><path d="M3 7l3 3 6-8" fill="none" stroke="#28a8e0" stroke-width="1.8"/></svg>Hydro Excavation</li>
      <li><svg class="tick" viewBox="0 0 14 14"><rect x="1" y="1" width="12" height="12" fill="none" stroke="#1d5fa8" stroke-width="1.2"/><path d="M3 7l3 3 6-8" fill="none" stroke="#28a8e0" stroke-width="1.8"/></svg>Hydro Jetting</li>
      <li><svg class="tick" viewBox="0 0 14 14"><rect x="1" y="1" width="12" height="12" fill="none" stroke="#1d5fa8" stroke-width="1.2"/><path d="M3 7l3 3 6-8" fill="none" stroke="#28a8e0" stroke-width="1.8"/></svg>Well Pumps</li>
      <li><svg class="tick" viewBox="0 0 14 14"><rect x="1" y="1" width="12" height="12" fill="none" stroke="#1d5fa8" stroke-width="1.2"/><path d="M3 7l3 3 6-8" fill="none" stroke="#28a8e0" stroke-width="1.8"/></svg>Sewer Pumps</li>
      <li><svg class="tick" viewBox="0 0 14 14"><rect x="1" y="1" width="12" height="12" fill="none" stroke="#1d5fa8" stroke-width="1.2"/><path d="M3 7l3 3 6-8" fill="none" stroke="#28a8e0" stroke-width="1.8"/></svg>Water Mains</li>
      <li><svg class="tick" viewBox="0 0 14 14"><rect x="1" y="1" width="12" height="12" fill="none" stroke="#1d5fa8" stroke-width="1.2"/><path d="M3 7l3 3 6-8" fill="none" stroke="#28a8e0" stroke-width="1.8"/></svg>Sewer Mains</li>
    </ul>

    <h2 class="section-title front__emergency-title">24/7 Emergency Services</h2>
    <ul class="sector-list">
      <li><svg class="star" viewBox="0 0 14 14"><circle cx="7" cy="7" r="7" fill="#e3232c"/><path d="M7 2.8l1.2 2.6 2.8.3-2.1 1.9.6 2.8L7 9l-2.5 1.4.6-2.8L3 5.7l2.8-.3z" fill="#fff"/></svg>Residential</li>
      <li><svg class="star" viewBox="0 0 14 14"><circle cx="7" cy="7" r="7" fill="#e3232c"/><path d="M7 2.8l1.2 2.6 2.8.3-2.1 1.9.6 2.8L7 9l-2.5 1.4.6-2.8L3 5.7l2.8-.3z" fill="#fff"/></svg>Commercial</li>
      <li><svg class="star" viewBox="0 0 14 14"><circle cx="7" cy="7" r="7" fill="#e3232c"/><path d="M7 2.8l1.2 2.6 2.8.3-2.1 1.9.6 2.8L7 9l-2.5 1.4.6-2.8L3 5.7l2.8-.3z" fill="#fff"/></svg>Industrial</li>
      <li><svg class="star" viewBox="0 0 14 14"><circle cx="7" cy="7" r="7" fill="#e3232c"/><path d="M7 2.8l1.2 2.6 2.8.3-2.1 1.9.6 2.8L7 9l-2.5 1.4.6-2.8L3 5.7l2.8-.3z" fill="#fff"/></svg>Municipal</li>
    </ul>
  </section>

  <!-- Back -->
  <section class="card card--back" aria-label="Back of card: contact">
    <svg class="back__shape" viewBox="0 0 540 309" preserveAspectRatio="none">
      <polygon points="255,309 420,150 540,215 540,309" fill="#e3232c"/>
      <polygon points="275,309 424,165 540,228 540,309" fill="#ffffff"/>
    </svg>

    <div class="back__notch">
      <span class="contact-icon"><svg viewBox="0 0 10 10"><rect x="1" y="2.5" width="8" height="5" fill="none" stroke="#fff" stroke-width="1"/><path d="M1 2.5l4 3 4-3" fill="none" stroke="#fff" stroke-width="1"/></svg></span>
      <span class="contact-icon"><svg viewBox="0 0 10 10"><path d="M2.5 1.5l1.5 0 .8 2-1 .8a5 5 0 0 0 2 2l.8-1 2 .8v1.5a1 1 0 0 1-1 1A7 7 0 0 1 1.5 2.5a1 1 0 0 1 1-1z" fill="#fff"/></svg></span>
      <span class="contact-icon"><svg viewBox="0 0 10 10"><rect x="3" y="1" width="4" height="8" rx="1" fill="none" stroke="#fff" stroke-width="1"/></svg></span>
      <span class="contact-icon"><svg viewBox="0 0 10 10"><circle cx="5" cy="5" r="3.6" fill="none" stroke="#fff" stroke-width="1"/><path d="M1.4 5h7.2M5 1.4c-2 2-2 5.2 0 7.2M5 1.4c2 2 2 5.2 0 7.2" fill="none" stroke="#fff" stroke-width=".8"/></svg></span>
    </div>

    <h1 class="back__name">Daniel Moreno</h1>
    <p class="back__role">Executive Director</p>
    <ul class="contact-list">
      <li>info@riverbendws.com</li>
      <li>+1 555 014 2207</li>
      <li>+1 555 014 2207</li>
      <li>www.riverbendws.com</li>
    </ul>
    <p class="back__address">Address: Suite 4, 21 Mill Street, Kingston NY 12401<br>Tax ID: 12 345 678 901</p>

    <div class="brand back__brand"><span class="brand__dot"></span><span>Riverbend<br>Water &amp; Sewer</span></div>
    <div class="social" aria-label="Social profiles"><span></span><span></span><span></span><span></span></div>
  </section>

</body>
</html>
```